KORVEL Company sign

We are building a new IT building and want to showcase that with a big sign on the block of land. We also want to utilize the sign and put it inside the office in the reception once it is built. We are a managed IT company and unique for the area we live. We have 18 staff and growing rapidly. We plan to be hear for a long time and providing jobs for the future. We want something catchy and that stands out and looks good. our target audience is corporate businesses and we highlight our level of responsiveness and care. Let me know if this is enough information to get started. It would be great to include that we are local supporting local.

Target Market(s)

Cooperate Businesses

```html
<!DOCTYPE html>
<html lang="en">
<head>
<meta charset="utf-8">
<title>KORVEL Company Sign</title>
<link href="https://fonts.googleapis.com/css2?family=Bebas+Neue&family=Montserrat:wght@400;600;800&display=swap" rel="stylesheet">
<style>
  :root {
    --canvas-bg: #8c8b8c;
    --navy: #0d4f8b;
    --blue: #1b86d0;
    --blue-deep: #0b5aa5;
    --ink: #2a2a2a;
    --slate: #3b3b3c;
    --paper: #f3f3f3;
    --paper-shade: #e6e6e7;
    --grey-text: #7a7a7a;
    --white: #ffffff;
  }
  * { box-sizing: border-box; margin: 0; padding: 0; }
  html, body { width: 1091px; height: 1200px; overflow: hidden; }
  body { background: var(--canvas-bg); position: relative; font-family: "Montserrat", sans-serif; }

  .sign {
    position: absolute; left: 40px; top: 431px;
    width: 1011px; height: 337px;
    background: var(--paper);
    box-shadow: 0 6px 14px rgba(0,0,0,.35);
    overflow: hidden;
  }
  .sign__shapes { position: absolute; inset: 0; }

  .headline { position: absolute; left: 41px; top: 20px; font-family: "Bebas Neue", sans-serif; font-weight: 400; line-height: .9; white-space: nowrap; }
  .headline__lead { display: block; font-size: 82px; color: var(--navy); }
  .headline__follow { display: block; font-size: 65px; color: var(--ink); margin-top: 2px; }

  .brand { position: absolute; left: 0; top: 0; }
  .brand__mark { position: absolute; left: 40px; top: 216px; width: 88px; height: 88px; border-radius: 50%; background: var(--blue); box-shadow: 0 0 0 4px var(--white); }
  .brand__name { position: absolute; left: 144px; top: 222px; font-family: "Montserrat", sans-serif; font-weight: 800; font-size: 56px; line-height: 1; color: var(--blue); letter-spacing: 1px; }
  .brand__tagline { position: absolute; left: 146px; top: 278px; white-space: nowrap; font-size: 13px; letter-spacing: 2.6px; color: var(--grey-text); }
  .brand__strip { position: absolute; left: 111px; top: 296px; width: 292px; height: 17px; border-radius: 0 9px 9px 0; background: var(--blue); color: var(--white); font-size: 11px; line-height: 17px; padding-left: 34px; white-space: nowrap; }

  .soon { position: absolute; left: 412px; top: 154px; width: 180px; height: 180px; border-radius: 50%;
    background: radial-gradient(circle at 40% 28%, #2c93dc, var(--blue-deep) 72%);
    border: 6px solid var(--white); box-shadow: 0 3px 8px rgba(0,0,0,.3);
    display: flex; align-items: center; justify-content: center; text-align: center;
    font-family: "Bebas Neue", sans-serif; font-size: 52px; line-height: .9; color: var(--white); }

  .phone { position: absolute; left: 641px; top: 231px; width: 337px; height: 54px; border-radius: 27px;
    background: var(--blue-deep); display: flex; align-items: center; padding-left: 9px; gap: 14px; }
  .phone__icon { width: 40px; height: 40px; border-radius: 50%; background: var(--white); display: flex; align-items: center; justify-content: center; flex: none; }
  .phone__number { font-size: 35px; font-weight: 800; color: var(--white); letter-spacing: 1px; white-space: nowrap; }

  .web { position: absolute; left: 634px; top: 288px; font-size: 33px; font-weight: 600; color: var(--white); white-space: nowrap; }
</style>
</head>
<body>
  <section class="sign">
    <svg class="sign__shapes" width="1011" height="337" viewBox="0 0 1011 337">
      <defs>
        <linearGradient id="photoTones" x1="0" y1="0" x2="0" y2="1">
          <stop offset="0" stop-color="#584547"/>
          <stop offset=".42" stop-color="#6a5759"/>
          <stop offset=".5" stop-color="#8a7f81"/>
          <stop offset=".55" stop-color="#e2e1e4"/>
          <stop offset="1" stop-color="#cbcacd"/>
        </linearGradient>
        <radialGradient id="photoLight" cx=".55" cy=".55" r=".5">
          <stop offset="0" stop-color="#ffffff" stop-opacity=".18"/>
          <stop offset="1" stop-color="#ffffff" stop-opacity="0"/>
        </radialGradient>
      </defs>
      <path d="M300 0 L420 0 L460 60 L400 150 L330 70 Z" fill="var(--paper-shade)" opacity=".7"/>
      <path d="M430 80 L500 150 L440 200 L380 140 Z" fill="var(--paper-shade)" opacity=".6"/>
      <path d="M0 158 C150 138 320 160 430 218 L430 240 C310 182 150 172 0 196 Z" fill="#1b86d0"/>
      <path d="M506 156 C515 70 575 18 656 0 L626 0 C556 22 496 80 488 156 Z" fill="#1b86d0"/>
      <g role="img" aria-label="Photo of two children in branded shirts playing with telephones, cables and a laptop">
        <path d="M530 156 C540 78 592 24 646 0 L1011 0 L1011 258 L560 258 Z" fill="url(#photoTones)"/>
        <path d="M530 156 C540 78 592 24 646 0 L1011 0 L1011 258 L560 258 Z" fill="url(#photoLight)"/>
      </g>
      <path d="M574 257 L1011 257 L1011 337 L606 337 Z" fill="#3b3b3c"/>
    </svg>

    <h1 class="headline">
      <span class="headline__lead">We are providing</span>
      <span class="headline__follow">Jobs for the future</span>
    </h1>

    <div class="brand">
      <div class="brand__strip">1300 555 018 · CORPORATE I.T. SERVICES</div>
      <div class="brand__mark"></div>
      <div class="brand__name">KORVEL</div>
      <div class="brand__tagline">NO EXCUSES. JUST RESULTS</div>
    </div>

    <div class="soon">Coming<br>Soon!</div>

    <div class="phone">
      <span class="phone__icon">
        <svg width="24" height="24" viewBox="0 0 24 24"><path d="M6.6 10.8a15 15 0 0 0 6.6 6.6l2.2-2.2c.3-.3.7-.4 1-.2 1.1.4 2.3.6 3.6.6.6 0 1 .4 1 1V20c0 .6-.4 1-1 1A17 17 0 0 1 3 4c0-.6.4-1 1-1h3.5c.6 0 1 .4 1 1 0 1.3.2 2.5.6 3.6.1.3 0 .7-.2 1z" fill="#0b5aa5"/></svg>
      </span>
      <span class="phone__number">1300 555 018</span>
    </div>
    <div class="web">www.korvel.com.au</div>
  </section>
</body>
</html>
```